Come See The One And Only - KVTO 2022 Tradeshow

Tradeshow:
- Need as a backdrop visual
- Size: 8' x 10' - Template attached with panels

Text needed on the backdrop:
"Come see
the ONE and ONLY
ONE-STOP-SHOP make ready provider
to see the easiest scheduled turn EVER known to man!
IT'S SHOWTIME!"

-Need the Vale Prime logo in the top right corner with it on a white circle like it is coming into the design and it is easy to see for branding.
- On the side panels "Make Ready Made Easy" & the website "www.valeprimeco.com" use the background of the side panels as a solid brand color.
- Our brand colors are attached as a screenshot to incorporate them into the design.
- The attachment that is 'vintage circus' is to show how to play around with the text we need and make it fun!

The theme of the show is "Under The Big Top" it is a circus theme! Give us something fun and cartoon looking works, such as a ring master and animals. If you want to submit clowns, make sure they are NOT scary looking!

tradeshow

• Covered by your Grace - Regular (Vale Prime font for the side panels to use)

• Vale Prime logo or branded colors
• circus theme to it
• no scary clowns

```html
<!DOCTYPE html>
<html lang="en">
<head>
<meta charset="utf-8">
<title>Under The Big Top – Vale Prime Backdrop</title>
<link rel="stylesheet" href="https://fonts.googleapis.com/css2?family=Rye&family=Sancreek&family=Holtwood+One+SC&display=swap">
<style>
  :root{
    --cream:#f8f3de;
    --orange:#d9532f;
    --salmon:#ef7a62;
    --navy:#1b4a68;
    --teal:#1aab9b;
    --slate:#8fa3ad;
    --ink:#141414;
    --white:#ffffff;
  }
  html,body{margin:0;padding:0;overflow:hidden;background:var(--white);}
  .canvas{width:1200px;height:806px;position:relative;overflow:hidden;background:var(--white);}
  .backdrop{display:block;width:1200px;height:806px;}
  .display{font-family:"Rye",serif;}
  .condensed{font-family:"Sancreek",serif;}
  .slab{font-family:"Holtwood One SC",serif;}
  .panel-text{font-family:"Holtwood One SC",serif;}
</style>
</head>
<body>
<div class="canvas">
<svg class="backdrop" viewBox="0 0 1200 806" xmlns="http://www.w3.org/2000/svg">
  <defs>
    <radialGradient id="burst" cx="50%" cy="52%" r="70%">
      <stop offset="0" stop-color="#f8f3de"/>
      <stop offset="0.45" stop-color="#efcfb4"/>
      <stop offset="1" stop-color="#d9532f"/>
    </radialGradient>
    <polygon id="star" points="0,-10 2.9,-3.1 9.5,-3.1 4.2,1.2 5.9,8.1 0,4 -5.9,8.1 -4.2,1.2 -9.5,-3.1 -2.9,-3.1"/>
  </defs>

  <!-- sunburst background area -->
  <rect class="sunburst" x="58" y="44" width="1084" height="676" fill="url(#burst)" role="img" aria-label="Vintage circus sunburst of orange, cream and slate rays"/>

  <!-- side panels -->
  <g class="side-panel side-panel--left">
    <rect x="90" y="96" width="53" height="570" fill="var(--navy)"/>
    <use href="#star" x="116" y="124" fill="var(--salmon)" transform="translate(0,0)"/>
    <use href="#star" x="116" y="172" fill="var(--teal)" transform="scale(1)"/>
    <text class="panel-text" transform="translate(110,381) rotate(-90)" text-anchor="middle" font-size="19" fill="var(--salmon)" textLength="340" lengthAdjust="spacingAndGlyphs">MAKE READY MADE EASY</text>
    <text class="panel-text" transform="translate(133,381) rotate(-90)" text-anchor="middle" font-size="11" fill="var(--cream)" textLength="270" lengthAdjust="spacingAndGlyphs">WWW.VALEPRIMECO.COM</text>
    <use href="#star" x="116" y="588" fill="var(--teal)"/>
    <use href="#star" x="116" y="638" fill="var(--salmon)"/>
  </g>
  <g class="side-panel side-panel--right">
    <rect x="1058" y="96" width="53" height="570" fill="var(--navy)"/>
    <use href="#star" x="1084" y="124" fill="var(--salmon)"/>
    <use href="#star" x="1084" y="172" fill="var(--teal)"/>
    <text class="panel-text" transform="translate(1090,381) rotate(90)" text-anchor="middle" font-size="19" fill="var(--salmon)" textLength="340" lengthAdjust="spacingAndGlyphs">MAKE READY MADE EASY</text>
    <text class="panel-text" transform="translate(1067,381) rotate(90)" text-anchor="middle" font-size="11" fill="var(--cream)" textLength="270" lengthAdjust="spacingAndGlyphs">WWW.VALEPRIMECO.COM</text>
    <use href="#star" x="1084" y="588" fill="var(--teal)"/>
    <use href="#star" x="1084" y="638" fill="var(--salmon)"/>
  </g>

  <!-- central teal sign -->
  <g class="sign-frame">
    <rect x="226" y="146" width="752" height="466" rx="46" fill="var(--navy)"/>
    <rect x="464" y="104" width="362" height="80" rx="34" fill="var(--navy)"/>
    <rect x="232" y="152" width="740" height="454" rx="40" fill="var(--teal)"/>
    <rect x="470" y="110" width="350" height="76" rx="28" fill="var(--teal)"/>
    <rect x="244" y="164" width="716" height="430" rx="32" fill="none" stroke="var(--cream)" stroke-width="2" stroke-dasharray="3 7"/>
  </g>

  <!-- headline -->
  <g class="headline">
    <g transform="translate(250,318) rotate(-14)">
      <text class="display" x="0" y="0" font-size="86" fill="var(--cream)" stroke="var(--orange)" stroke-width="4" paint-order="stroke" textLength="320" lengthAdjust="spacingAndGlyphs">COME SEE</text>
    </g>
    <text class="display" x="576" y="172" font-size="26" fill="var(--cream)" textLength="56" lengthAdjust="spacingAndGlyphs">THE</text>
    <text class="display" x="576" y="226" font-size="54" fill="var(--cream)" stroke="var(--navy)" stroke-width="2" paint-order="stroke" textLength="104" lengthAdjust="spacingAndGlyphs">ONE</text>
    <text class="display" x="690" y="214" font-size="22" fill="var(--cream)" textLength="56" lengthAdjust="spacingAndGlyphs">AND</text>
    <text class="display" x="680" y="274" font-size="54" fill="var(--cream)" stroke="var(--navy)" stroke-width="2" paint-order="stroke" textLength="124" lengthAdjust="spacingAndGlyphs">ONLY</text>
    <use href="#star" x="562" y="264" fill="var(--orange)"/>
    <use href="#star" x="598" y="258" fill="var(--orange)" transform="translate(598,258) scale(1.4) translate(-598,-258)"/>
    <use href="#star" x="636" y="264" fill="var(--orange)"/>
  </g>

  <!-- one-stop-shop banner -->
  <g class="shop-banner">
    <rect x="400" y="302" width="402" height="92" rx="6" fill="var(--navy)"/>
    <rect x="402" y="304" width="396" height="86" rx="6" fill="var(--orange)"/>
    <rect x="410" y="312" width="380" height="70" rx="4" fill="none" stroke="var(--cream)" stroke-width="2"/>
    <text class="condensed" x="600" y="370" text-anchor="middle" font-size="64" fill="var(--cream)" textLength="360" lengthAdjust="spacingAndGlyphs">ONE-STOP-SHOP</text>
  </g>

  <text class="display" x="598" y="436" text-anchor="middle" font-size="30" fill="var(--ink)" textLength="334" lengthAdjust="spacingAndGlyphs">MAKE READY PROVIDER</text>
  <rect class="star-band" x="425" y="449" width="350" height="11" fill="var(--cream)"/>
  <g fill="var(--orange)">
    <circle cx="440" cy="454.5" r="2"/><circle cx="470" cy="454.5" r="2"/><circle cx="500" cy="454.5" r="2"/><circle cx="530" cy="454.5" r="2"/><circle cx="560" cy="454.5" r="2"/><circle cx="590" cy="454.5" r="2"/><circle cx="620" cy="454.5" r="2"/><circle cx="650" cy="454.5" r="2"/><circle cx="680" cy="454.5" r="2"/><circle cx="710" cy="454.5" r="2"/><circle cx="740" cy="454.5" r="2"/><circle cx="765" cy="454.5" r="2"/>
  </g>

  <g class="tagline">
    <text class="slab" x="414" y="489" font-size="17" fill="var(--ink)" textLength="214" lengthAdjust="spacingAndGlyphs">TO SEE THE EASIEST</text>
    <text class="slab" x="446" y="513" font-size="17" fill="var(--ink)" textLength="202" lengthAdjust="spacingAndGlyphs">SCHEDULED TURN</text>
    <text class="display" x="656" y="514" font-size="46" fill="var(--orange)" stroke="var(--cream)" stroke-width="1.5" paint-order="stroke" textLength="116" lengthAdjust="spacingAndGlyphs">EVER</text>
    <rect x="424" y="526" width="136" height="12" fill="var(--cream)"/>
    <g fill="var(--salmon)">
      <use href="#star" x="440" y="532" transform="translate(440,532) scale(0.45) translate(-440,-532)"/>
      <use href="#star" x="462" y="532" transform="translate(462,532) scale(0.45) translate(-462,-532)"/>
      <use href="#star" x="484" y="532" transform="translate(484,532) scale(0.45) translate(-484,-532)"/>
      <use href="#star" x="506" y="532" transform="translate(506,532) scale(0.45) translate(-506,-532)"/>
      <use href="#star" x="528" y="532" transform="translate(528,532) scale(0.45) translate(-528,-532)"/>
      <use href="#star" x="548" y="532" transform="translate(548,532) scale(0.45) translate(-548,-532)"/>
    </g>
    <text class="slab" x="588" y="539" font-size="17" fill="var(--ink)" textLength="180" lengthAdjust="spacingAndGlyphs">KNOWN TO MAN!</text>
  </g>

  <!-- illustrations -->
  <rect class="illustration illustration--elephant" x="232" y="364" width="156" height="196" rx="40" fill="#b9b9b9" role="img" aria-label="Cartoon elephant in a party hat balancing on a striped circus ball"/>
  <rect class="illustration illustration--juggler" x="806" y="326" width="172" height="226" rx="40" fill="#e59a86" role="img" aria-label="Cartoon juggler in a striped shirt juggling balls on a circus pedestal"/>

  <!-- showtime -->
  <text class="display showtime" x="600" y="632" text-anchor="middle" font-size="100" fill="var(--ink)" stroke="var(--cream)" stroke-width="8" paint-order="stroke" textLength="640" lengthAdjust="spacingAndGlyphs">IT'S SHOWTIME!</text>

  <!-- brand badge -->
  <g class="brand-badge">
    <circle cx="890" cy="188" r="88" fill="var(--orange)"/>
    <circle cx="890" cy="188" r="80" fill="none" stroke="var(--cream)" stroke-width="2" stroke-dasharray="2 6"/>
    <circle cx="890" cy="188" r="72" fill="var(--white)" stroke="var(--navy)" stroke-width="3"/>
    <text class="display" x="890" y="180" text-anchor="middle" font-size="26" fill="var(--navy)" textLength="90" lengthAdjust="spacingAndGlyphs">VALE</text>
    <text class="display" x="890" y="214" text-anchor="middle" font-size="26" fill="var(--navy)" textLength="108" lengthAdjust="spacingAndGlyphs">PRIME</text>
  </g>
</svg>
</div>
</body>
</html>
```